Author Website Design

The purpose of the site will be to promote "Harbor," an edgy new thriller from Marcus Pellerin. I'd like the site to correspond with the design and colors of the book's cover, as I'm focused on creating a recognizable brand. Designers are of course encouraged to put their own artistic stamp on the project, but its important to integrate the site's design with the cover.

Requirements
Must have
• Site must be integrated with/correspond to the design of my book cover. The site should have the following pages: About; Books; Velm Quarter; Contact; Blog.

The site should link readers to the various retailers where Harbor is available

```html
<!DOCTYPE html>
<html lang="en">
<head>
<meta charset="utf-8">
<title>Harbor — Marcus Pellerin</title>
<link rel="stylesheet" href="https://fonts.googleapis.com/css2?family=Oswald:wght@700&family=Cambo&display=swap">
<style>
  :root {
    --ink: #030305;
    --gold: #f6cf12;
    --gold-soft: #f2d23a;
    --rule: #8c7d3c;
    --frame: #6f5d0c;
    --city-sky: #2b3340;
    --city-glow: #6a5228;
    --city-deep: #0b0b0e;
  }
  * { margin: 0; padding: 0; box-sizing: border-box; }
  html, body {
    width: 1200px;
    height: 812px;
    overflow: hidden;
    background: var(--ink);
  }
  .page {
    position: relative;
    width: 1200px;
    height: 812px;
    background: var(--ink);
    color: var(--gold);
    font-family: Arial, Helvetica, sans-serif;
  }
  .brand {
    position: absolute;
    top: 50px;
    left: 0;
    width: 100%;
    text-align: center;
  }
  .brand-title {
    font-family: "Oswald", sans-serif;
    font-weight: 700;
    font-size: 78px;
    line-height: 94px;
    letter-spacing: 2px;
    color: var(--gold);
  }
  .brand-author {
    font-family: "Oswald", sans-serif;
    font-weight: 700;
    font-size: 20px;
    line-height: 24px;
    letter-spacing: 1px;
    color: var(--gold);
    margin-top: 10px;
  }
  .main-nav {
    position: absolute;
    top: 193px;
    left: 68px;
    width: 1063px;
    height: 53px;
    border-top: 1px solid var(--rule);
    border-bottom: 1px solid var(--rule);
    display: flex;
    justify-content: center;
    align-items: center;
    gap: 84px;
    padding-left: 6px;
  }
  .main-nav a {
    font-family: "Cambo", serif;
    font-size: 26px;
    color: var(--gold);
    text-decoration: none;
    letter-spacing: 0.5px;
  }
  .city-art {
    position: absolute;
    top: 258px;
    left: 470px;
    width: 730px;
    height: 480px;
    background:
      radial-gradient(ellipse at 28% 40%, rgba(200,180,140,0.35), transparent 35%),
      radial-gradient(ellipse at 60% 55%, var(--city-glow), transparent 55%),
      linear-gradient(180deg, var(--city-sky) 0%, #3a3326 45%, #2a2115 70%, var(--city-deep) 100%);
    -webkit-mask-image: linear-gradient(90deg, transparent 0%, #000 18%, #000 100%);
    mask-image: linear-gradient(90deg, transparent 0%, #000 18%, #000 100%);
    opacity: 0.95;
  }
  .city-art::after {
    content: "";
    position: absolute;
    inset: 0;
    background: linear-gradient(180deg, transparent 70%, var(--ink) 100%);
  }
  .story-panel {
    position: absolute;
    top: 291px;
    left: 68px;
    width: 473px;
    height: 412px;
    border: 3px solid var(--frame);
    border-radius: 6px;
    background: rgba(0, 0, 0, 0.62);
    padding: 47px 22px 0 28px;
  }
  .story-panel p {
    font-size: 13.4px;
    line-height: 17px;
    color: var(--gold);
    margin-bottom: 17px;
  }
  .story-panel .welcome {
    font-size: 16px;
    font-weight: 700;
    font-style: italic;
    margin-top: 20px;
  }
  .site-footer {
    position: absolute;
    top: 765px;
    left: 68px;
    width: 1063px;
    border-top: 1px solid var(--rule);
    display: flex;
    justify-content: space-between;
    padding: 9px 0 0 3px;
    font-size: 11.5px;
    color: var(--gold-soft);
  }
  .site-footer strong { font-weight: 700; color: var(--gold); }
  .footer-nav a {
    color: var(--gold-soft);
    text-decoration: none;
  }
</style>
</head>
<body>
<div class="page">
  <header class="brand">
    <div class="brand-title">HARBOR</div>
    <div class="brand-author">MARCUS PELLERIN</div>
  </header>

  <nav class="main-nav">
    <a href="#">About</a>
    <a href="#">Books</a>
    <a href="#">Velm Quarter</a>
    <a href="#">Blog</a>
    <a href="#">Contact</a>
  </nav>

  <div class="city-art" role="img" aria-label="Night cityscape of towering skyscrapers with helicopters, a giant billboard and a wrecked car under a stormy sky"></div>

  <section class="story-panel">
    <p>In a secret laboratory hidden under the desert, a covert bioengineering project-codename “Exodus”-has discovered the gene responsible for the human soul.</p>
    <p>Somewhere in the neon sprawl outside the nation’s collapsing economic core, a group of renegade monks are on the verge of uncovering a secret that has eluded mankind for centuries.</p>
    <p>In a glittering tower high above the urban decay, an ascendant U.S. Senator is found dead-an apparent, yet inexplicable, suicide.</p>
    <p>And in the streets below, a young man races through an ultra modern metropolis on the verge of a violent revolution....closing in on the terrible truth behind Exodus-and one man’s dark vision for the future of mankind.</p>
    <p class="welcome">Welcome to Velm Quarter.</p>
  </section>

  <footer class="site-footer">
    <span>All Rights Reserved@2011, <strong>Harbor</strong></span>
    <span class="footer-nav"><a href="#">About</a> | <a href="#">Books</a> | <a href="#">Velm Quarter</a> | <a href="#">Blog</a> | <a href="#">Contact</a></span>
  </footer>
</div>
</body>
</html>
```